vireLattice "organisation chart"

We need a new Organisation Chart for our Company! We are actually in a Change-management-process and will Change from a hierarchical Organisation in to a Network Organisation. Therefor we need a new Organisation Chart.
The following departements must be visible and legible on the Chart:
Team Sales & Consulting
Team Productmanagement
Team Supply Chain
Team Human Resources
Team Smart Digital Development
Team Marketing & Communication
The title of the Chart ist «vireLattice»
The Colors of the back of the Chart must be: RGB 73/25/102 // Pantone 2627
The Colors for the different Teams should be:
Team Sales & Consulting (Pantone: 803/neon yellow = Background)
Team Productmanagement (Pantone: 804/neon orange = Background)
Team Supply Chain (Pantone: 802/neon green = Background)
Team Human Resources (Pantone: 801/neon blue = Background)
Team Smart Digital Development (Pantone: 805/neon red = Background)
Team Marketing & Communication (Pantone: 803/neon pink = Background)
See below (upload files) an example showing a self-made Chart ... :-)
Our font is: Univers LT Std // Please feel free to Combine the Fonts Colors with the background colors
It Company

```html
<!DOCTYPE html>
<html lang="en">
<head>
<meta charset="utf-8">
<title>vireLattice – Organisation Chart</title>
<link href="https://fonts.googleapis.com/css2?family=Questrial&display=swap" rel="stylesheet">
<style>
  :root {
    --bg: #472462;
    --ink: #472462;
    --white: #ffffff;
    --yellow: #f8ea1c;
    --pink: #e84f9e;
    --green: #5fbf46;
    --red: #ef5258;
    --orange: #f7a44a;
    --blue: #1b9ad3;
    --shadow: #1e0b2c;
  }
  html, body {
    margin: 0;
    padding: 0;
    width: 1200px;
    height: 1200px;
    overflow: hidden;
    background: var(--bg);
  }
  .org-chart {
    display: block;
    width: 1200px;
    height: 1200px;
    font-family: "Questrial", "Century Gothic", sans-serif;
  }
  .team-label {
    fill: var(--ink);
    font-size: 32px;
    text-anchor: middle;
    dominant-baseline: middle;
  }
  .hub-title {
    fill: var(--white);
    font-size: 30px;
    text-anchor: middle;
    dominant-baseline: middle;
  }
  .icon-ring { fill: var(--bg); stroke-width: 7; }
  .link { fill: none; stroke-width: 12; }
  .hub-ring { fill: none; stroke-width: 8; }
</style>
</head>
<body>
<svg class="org-chart" viewBox="0 0 1200 1200" xmlns="http://www.w3.org/2000/svg">
  <defs>
    <radialGradient id="glow-yellow" cx="50%" cy="50%" r="55%"><stop offset="0" stop-color="#fff"/><stop offset="0.75" stop-color="var(--yellow)"/></radialGradient>
    <radialGradient id="glow-pink" cx="50%" cy="50%" r="55%"><stop offset="0" stop-color="#fff"/><stop offset="0.75" stop-color="var(--pink)"/></radialGradient>
    <radialGradient id="glow-green" cx="50%" cy="50%" r="55%"><stop offset="0" stop-color="#fff"/><stop offset="0.75" stop-color="var(--green)"/></radialGradient>
    <radialGradient id="glow-red" cx="50%" cy="50%" r="55%"><stop offset="0" stop-color="#fff"/><stop offset="0.75" stop-color="var(--red)"/></radialGradient>
    <radialGradient id="glow-orange" cx="50%" cy="50%" r="55%"><stop offset="0" stop-color="#fff"/><stop offset="0.75" stop-color="var(--orange)"/></radialGradient>
    <radialGradient id="glow-blue" cx="50%" cy="50%" r="55%"><stop offset="0" stop-color="#fff"/><stop offset="0.75" stop-color="var(--blue)"/></radialGradient>

    <linearGradient id="link-sales-marketing" gradientUnits="userSpaceOnUse" x1="532" y1="0" x2="672" y2="0"><stop offset="0" stop-color="var(--yellow)"/><stop offset="1" stop-color="var(--pink)"/></linearGradient>
    <linearGradient id="link-marketing-supply" gradientUnits="userSpaceOnUse" x1="828" y1="384" x2="896" y2="508"><stop offset="0" stop-color="var(--pink)"/><stop offset="1" stop-color="var(--green)"/></linearGradient>
    <linearGradient id="link-supply-digital" gradientUnits="userSpaceOnUse" x1="908" y1="692" x2="828" y2="812"><stop offset="0" stop-color="var(--green)"/><stop offset="1" stop-color="var(--red)"/></linearGradient>
    <linearGradient id="link-digital-product" gradientUnits="userSpaceOnUse" x1="672" y1="0" x2="532" y2="0"><stop offset="0" stop-color="var(--red)"/><stop offset="1" stop-color="var(--orange)"/></linearGradient>
    <linearGradient id="link-product-hr" gradientUnits="userSpaceOnUse" x1="376" y1="812" x2="296" y2="692"><stop offset="0" stop-color="var(--orange)"/><stop offset="1" stop-color="var(--blue)"/></linearGradient>
    <linearGradient id="link-hr-sales" gradientUnits="userSpaceOnUse" x1="296" y1="508" x2="372" y2="384"><stop offset="0" stop-color="var(--blue)"/><stop offset="1" stop-color="var(--yellow)"/></linearGradient>

    <marker id="head-yellow" viewBox="0 0 10 10" refX="3" refY="5" markerWidth="3.4" markerHeight="3.4" orient="auto-start-reverse"><path d="M0 0 L10 5 L0 10 L3 5 Z" fill="var(--yellow)"/></marker>
    <marker id="head-pink" viewBox="0 0 10 10" refX="3" refY="5" markerWidth="3.4" markerHeight="3.4" orient="auto-start-reverse"><path d="M0 0 L10 5 L0 10 L3 5 Z" fill="var(--pink)"/></marker>
    <marker id="head-green" viewBox="0 0 10 10" refX="3" refY="5" markerWidth="3.4" markerHeight="3.4" orient="auto-start-reverse"><path d="M0 0 L10 5 L0 10 L3 5 Z" fill="var(--green)"/></marker>
    <marker id="head-red" viewBox="0 0 10 10" refX="3" refY="5" markerWidth="3.4" markerHeight="3.4" orient="auto-start-reverse"><path d="M0 0 L10 5 L0 10 L3 5 Z" fill="var(--red)"/></marker>
    <marker id="head-orange" viewBox="0 0 10 10" refX="3" refY="5" markerWidth="3.4" markerHeight="3.4" orient="auto-start-reverse"><path d="M0 0 L10 5 L0 10 L3 5 Z" fill="var(--orange)"/></marker>
    <marker id="head-blue" viewBox="0 0 10 10" refX="3" refY="5" markerWidth="3.4" markerHeight="3.4" orient="auto-start-reverse"><path d="M0 0 L10 5 L0 10 L3 5 Z" fill="var(--blue)"/></marker>
  </defs>

  <rect class="canvas-bg" width="1200" height="1200" fill="var(--bg)"/>

  <!-- Team discs -->
  <g class="team-discs">
    <circle cx="374" cy="206" r="137" fill="var(--shadow)"/><circle cx="370" cy="202" r="137" fill="url(#glow-yellow)"/>
    <circle cx="834" cy="206" r="137" fill="var(--shadow)"/><circle cx="830" cy="202" r="137" fill="url(#glow-pink)"/>
    <circle cx="146" cy="604" r="137" fill="var(--shadow)"/><circle cx="142" cy="600" r="137" fill="url(#glow-blue)"/>
    <circle cx="1062" cy="604" r="137" fill="var(--shadow)"/><circle cx="1058" cy="600" r="137" fill="url(#glow-green)"/>
    <circle cx="374" cy="1002" r="137" fill="var(--shadow)"/><circle cx="370" cy="998" r="137" fill="url(#glow-orange)"/>
    <circle cx="834" cy="1002" r="137" fill="var(--shadow)"/><circle cx="830" cy="998" r="137" fill="url(#glow-red)"/>
  </g>

  <!-- Icon rings -->
  <g class="icon-rings">
    <circle cx="438" cy="322" r="84" fill="var(--bg)"/><circle class="icon-ring" cx="438" cy="322" r="76" stroke="var(--yellow)"/>
    <circle cx="760" cy="322" r="84" fill="var(--bg)"/><circle class="icon-ring" cx="760" cy="322" r="76" stroke="var(--pink)"/>
    <circle cx="278" cy="600" r="84" fill="var(--bg)"/><circle class="icon-ring" cx="278" cy="600" r="76" stroke="var(--blue)"/>
    <circle cx="920" cy="600" r="84" fill="var(--bg)"/><circle class="icon-ring" cx="920" cy="600" r="76" stroke="var(--green)"/>
    <circle cx="438" cy="878" r="84" fill="var(--bg)"/><circle class="icon-ring" cx="438" cy="878" r="76" stroke="var(--orange)"/>
    <circle cx="760" cy="878" r="84" fill="var(--bg)"/><circle class="icon-ring" cx="760" cy="878" r="76" stroke="var(--red)"/>
  </g>

  <!-- Icons -->
  <g class="icon icon-sales" fill="var(--yellow)">
    <rect x="411" y="334" width="8" height="16"/><rect x="424" y="324" width="8" height="26"/>
    <rect x="437" y="318" width="8" height="32"/><rect x="450" y="310" width="8" height="40"/>
    <path d="M406 328 L428 306 L440 316 L458 296" fill="none" stroke="var(--yellow)" stroke-width="5"/>
    <path d="M450 290 L466 286 L462 302 Z"/>
  </g>
  <g class="icon icon-marketing" fill="var(--pink)">
    <path d="M728 314 L744 310 L772 294 L772 346 L744 330 L728 330 Z"/>
    <path d="M736 330 L744 330 L740 350 L734 350 Z"/>
    <g stroke="var(--pink)" stroke-width="4" stroke-linecap="round">
      <line x1="782" y1="304" x2="792" y2="296"/><line x1="784" y1="316" x2="796" y2="314"/>
      <line x1="784" y1="328" x2="796" y2="332"/><line x1="782" y1="340" x2="792" y2="348"/>
    </g>
  </g>
  <g class="icon icon-hr" fill="var(--blue)">
    <circle cx="254" cy="586" r="7"/><circle cx="302" cy="586" r="7"/><circle cx="278" cy="583" r="9"/>
    <path d="M240 614 Q240 596 254 596 Q268 596 268 614 Z"/>
    <path d="M288 614 Q288 596 302 596 Q316 596 316 614 Z"/>
    <path d="M260 622 Q260 596 278 596 Q296 596 296 622 Z"/>
    <path d="M276 598 L280 598 L281 616 L278 620 L275 616 Z" fill="var(--bg)"/>
  </g>
  <g class="icon icon-supply" fill="none" stroke="var(--green)" stroke-width="8" stroke-linecap="round">
    <path d="M912 612 L900 624 Q892 632 900 640 Q908 648 916 640 L928 628"/>
    <path d="M928 588 L940 576 Q948 568 940 560 Q932 552 924 560 L912 572"/>
    <line x1="912" y1="612" x2="928" y2="588"/>
  </g>
  <g class="icon icon-product" fill="none" stroke="var(--orange)">
    <circle cx="424" cy="890" r="16" stroke-width="8" stroke-dasharray="5 4"/>
    <circle cx="424" cy="890" r="7" stroke-width="5"/>
    <circle cx="458" cy="860" r="11" stroke-width="7" stroke-dasharray="4 3"/>
    <circle cx="458" cy="860" r="4" stroke-width="4"/>
  </g>
  <g class="icon icon-digital" fill="none" stroke="var(--red)" stroke-width="5">
    <rect x="756" y="852" width="38" height="30" rx="3"/>
    <rect x="740" y="866" width="22" height="34" rx="3"/>
    <rect x="726" y="882" width="14" height="20" rx="2"/>
    <line x1="770" y1="892" x2="784" y2="892"/>
  </g>

  <!-- Peer links -->
  <g class="peer-links">
    <path class="link" d="M532 296 Q600 232 672 296" stroke="url(#link-sales-marketing)" marker-start="url(#head-yellow)" marker-end="url(#head-pink)"/>
    <path class="link" d="M832 392 Q890 430 892 500" stroke="url(#link-marketing-supply)" marker-start="url(#head-pink)" marker-end="url(#head-green)"/>
    <path class="link" d="M904 700 Q900 780 832 806" stroke="url(#link-supply-digital)" marker-start="url(#head-green)" marker-end="url(#head-red)"/>
    <path class="link" d="M672 904 Q600 968 532 904" stroke="url(#link-digital-product)" marker-start="url(#head-red)" marker-end="url(#head-orange)"/>
    <path class="link" d="M372 806 Q304 780 300 700" stroke="url(#link-product-hr)" marker-start="url(#head-orange)" marker-end="url(#head-blue)"/>
    <path class="link" d="M300 500 Q306 430 368 392" stroke="url(#link-hr-sales)" marker-start="url(#head-blue)" marker-end="url(#head-yellow)"/>
  </g>

  <!-- Hub links -->
  <g class="hub-links">
    <path class="link" d="M536 468 Q545 420 500 400" stroke="var(--yellow)" marker-end="url(#head-yellow)"/>
    <path class="link" d="M684 472 Q730 460 726 412" stroke="var(--pink)" marker-end="url(#head-pink)"/>
    <path class="link" d="M748 612 Q770 645 824 612" stroke="var(--green)" marker-end="url(#head-green)"/>
    <path class="link" d="M666 732 Q660 790 702 800" stroke="var(--red)" marker-end="url(#head-red)"/>
    <path class="link" d="M516 724 Q480 730 474 788" stroke="var(--orange)" marker-end="url(#head-orange)"/>
    <path class="link" d="M456 596 Q420 560 376 592" stroke="var(--blue)" marker-end="url(#head-blue)"/>
  </g>

  <!-- Hub -->
  <g class="hub">
    <circle cx="604" cy="604" r="132" fill="var(--shadow)"/>
    <circle cx="600" cy="600" r="132" fill="var(--bg)"/>
    <g transform="rotate(-90 600 600)">
      <circle class="hub-ring" cx="600" cy="600" r="128" stroke="var(--pink)"   stroke-dasharray="134 671" stroke-dashoffset="0"/>
      <circle class="hub-ring" cx="600" cy="600" r="128" stroke="var(--green)"  stroke-dasharray="134 671" stroke-dashoffset="-134"/>
      <circle class="hub-ring" cx="600" cy="600" r="128" stroke="var(--red)"    stroke-dasharray="134 671" stroke-dashoffset="-268"/>
      <circle class="hub-ring" cx="600" cy="600" r="128" stroke="var(--orange)" stroke-dasharray="134 671" stroke-dashoffset="-402"/>
      <circle class="hub-ring" cx="600" cy="600" r="128" stroke="var(--blue)"   stroke-dasharray="134 671" stroke-dashoffset="-536"/>
      <circle class="hub-ring" cx="600" cy="600" r="128" stroke="var(--yellow)" stroke-dasharray="135 671" stroke-dashoffset="-670"/>
    </g>
    <text class="hub-title" x="600" y="604">vireLattice</text>
  </g>

  <!-- Team labels -->
  <g class="team-labels">
    <text class="team-label" x="368"><tspan x="368" y="124">Team</tspan><tspan x="368" y="158">Sales</tspan><tspan x="368" y="193">&amp; Consulting</tspan></text>
    <text class="team-label" x="830"><tspan x="830" y="118">Team</tspan><tspan x="830" y="151">Marketing &amp;</tspan><tspan x="830" y="186">Communication</tspan></text>
    <text class="team-label" x="102"><tspan x="102" y="568">Team</tspan><tspan x="102" y="602">Human</tspan><tspan x="102" y="636">Resources</tspan></text>
    <text class="team-label" x="1086"><tspan x="1086" y="560">Team</tspan><tspan x="1086" y="594">Supply</tspan><tspan x="1086" y="628">Chain</tspan></text>
    <text class="team-label" x="368"><tspan x="368" y="981">Team</tspan><tspan x="368" y="1015">Product</tspan><tspan x="368" y="1050">Management</tspan></text>
    <text class="team-label" x="830"><tspan x="830" y="989">Team</tspan><tspan x="830" y="1023">Smart Digital</tspan><tspan x="830" y="1058">Development</tspan></text>
  </g>
</svg>
</body>
</html>
```